I am looking for a book cover designs. The title of the book is "Ways to stand out and where your habits slip"

the book is not too formal but it is also not informal.

I wish for the title to be easily readable and capturing, especially the "ways to stand out" part.

the book should also include the author name: Tobar Kessly

everyone

• Full title and author name: Tobar Kessly
• There is a chapter that is called "turn the lamp inward", if you wish to do an illustration as part of the cover then perhaps that can give you an idea of what to go with.
• anything that takes attention away from the title.Also should not include any photographs.

```html
<!DOCTYPE html>
<html lang="en">
<head>
<meta charset="utf-8">
<title>Ways to Stand Out and Where Your Habits Slip — Tobar Kessly</title>
<link rel="stylesheet" href="https://fonts.googleapis.com/css2?family=Montserrat:wght@600;700&display=swap">
<style>
  :root {
    --backdrop: #7b7c7e;
    --cover-black: #050505;
    --portrait-dark: #0b0b0b;
    --portrait-mid: #3a3a3a;
    --portrait-light: #6e6e6e;
    --title-orange: #f08c00;
    --subtitle-grey: #c9cacd;
    --author-white: #ffffff;
  }
  * { margin: 0; padding: 0; box-sizing: border-box; }
  html, body {
    width: 1200px;
    height: 1200px;
    overflow: hidden;
    background: var(--backdrop);
  }
  .book-cover {
    position: absolute;
    left: 243px;
    top: 60px;
    width: 714px;
    height: 1080px;
    background: var(--cover-black);
    overflow: hidden;
    box-shadow: 0 10px 30px rgba(0, 0, 0, 0.35);
    font-family: "Montserrat", "Helvetica Neue", Arial, sans-serif;
  }
  .cover-portrait {
    position: absolute;
    inset: 0;
    background:
      radial-gradient(ellipse 55% 45% at 78% 48%, var(--portrait-light) 0%, var(--portrait-mid) 45%, transparent 100%),
      radial-gradient(ellipse 60% 70% at 85% 55%, var(--portrait-mid) 0%, var(--portrait-dark) 70%),
      linear-gradient(90deg, var(--cover-black) 0%, var(--cover-black) 35%, transparent 70%);
  }
  .title-line {
    position: absolute;
    left: 91px;
    white-space: nowrap;
    line-height: 1;
  }
  .title-main {
    color: var(--title-orange);
    font-weight: 700;
    font-size: 88px;
    letter-spacing: 0.02em;
  }
  .title-main.line-one { top: 178px; letter-spacing: 0.09em; }
  .title-main.line-two { top: 375px; }
  .title-sub {
    color: var(--subtitle-grey);
    font-weight: 700;
    font-size: 64px;
    letter-spacing: -0.02em;
  }
  .title-sub.line-three { top: 568px; }
  .title-sub.line-four { top: 761px; }
  .author-name {
    position: absolute;
    left: 91px;
    top: 952px;
    color: var(--author-white);
    font-weight: 600;
    font-size: 64px;
    letter-spacing: 0.16em;
    white-space: nowrap;
    line-height: 1;
  }
</style>
</head>
<body>
  <article class="book-cover">
    <div class="cover-portrait" role="img" aria-label="Dark black-and-white close-up portrait lit from the right side"></div>
    <h1 class="book-title">
      <span class="title-line title-main line-one">WAYS TO</span>
      <span class="title-line title-main line-two">STAND OUT</span>
      <span class="title-line title-sub line-three">&amp; WHERE YOUR</span>
      <span class="title-line title-sub line-four">HABITS SLIP</span>
    </h1>
    <p class="author-name">TOBAR KESSLY</p>
  </article>
</body>
</html>
```